Law Firm Needs Brochure Redesign Using New Logo

We are a personal injury law firm that does auto injuries and other personal injury cases. We want a new brochure that has our updated logo and information. Instead of gold and black, we want more navy, as matches the new logo. The Auto Liability portion should read: "(required by the state of Arizona in the amounts of $25,000 per person / $50,000 per accident, but a higher amount may be best )." The other information can remain the same. We'd like the brochure to keep the same professional tone as the previous brochure.
Our website is https://www.marbrenlegal.com/.

```html
<!DOCTYPE html>
<html lang="en">
<head>
<meta charset="utf-8">
<title>Marbren Legal – Car Accident Brochure</title>
<link href="https://fonts.googleapis.com/css2?family=Montserrat:wght@300;400;500;600;700&display=swap" rel="stylesheet">
<style>
  :root {
    --navy: #2b3a5e;
    --navy-deep: #1c2744;
    --gold: #e9a93a;
    --ink: #3a3f4a;
    --white: #ffffff;
    --panel-grey: #ececec;
    --canvas: #b4b4b4;
    --black: #0b0b0c;
  }
  * { box-sizing: border-box; margin: 0; padding: 0; }
  html, body { width: 1200px; height: 1200px; overflow: hidden; }
  body {
    background: var(--canvas);
    font-family: "Montserrat", sans-serif;
    color: var(--ink);
    position: relative;
  }
  .sheet {
    position: absolute;
    left: 273px;
    width: 654px;
    height: 505px;
    display: flex;
  }
  .sheet--outside { top: 61px; }
  .sheet--inside { top: 632px; }
  .panel { position: relative; height: 100%; overflow: hidden; }

  /* Outside: stats panel */
  .panel--stats { width: 215px; color: var(--white); text-align: center; }
  .photo-road {
    position: absolute; inset: 0;
    background: linear-gradient(180deg, #3c4a4e 0%, #4d5b70 35%, #6b7594 60%, #3f4966 85%, #2d3650 100%);
  }
  .stat { position: absolute; left: 0; right: 0; }
  .stat__over { color: var(--gold); font-size: 18px; font-weight: 500; line-height: 1; }
  .stat__number { color: var(--gold); font-size: 38px; font-weight: 700; line-height: 1; letter-spacing: -0.5px; }
  .stat__caption { font-size: 8.6px; font-weight: 300; line-height: 11px; padding: 2px 26px 0; }
  .stat--crashes { top: 34px; }
  .stat--fatal { top: 150px; }
  .brand { display: flex; align-items: center; gap: 6px; }
  .brand__dot { width: 14px; height: 14px; border-radius: 50%; background: var(--navy-deep); flex: none; }
  .brand__name { font-weight: 700; color: var(--navy-deep); letter-spacing: 1px; text-transform: uppercase; line-height: 1; }
  .panel--stats .brand { position: absolute; top: 267px; left: 0; right: 0; justify-content: center; }
  .panel--stats .brand__name { font-size: 14px; }
  .promise { position: absolute; top: 387px; left: 18px; right: 18px; font-size: 8.6px; font-weight: 300; line-height: 10.8px; }
  .promise strong { display: block; font-size: 11px; font-weight: 600; margin-top: 2px; }

  /* Outside: mailing panel */
  .panel--mailer { width: 220px; background: var(--white); }
  .panel--mailer .brand { position: absolute; top: 424px; left: 22px; }
  .panel--mailer .brand__name { font-size: 11px; }
  .panel--mailer .brand__dot { width: 12px; height: 12px; }
  .mailer__address { position: absolute; top: 456px; left: 22px; font-size: 8.6px; line-height: 11px; color: var(--ink); }

  /* Outside: cover panel */
  .panel--cover { width: 219px; background: var(--black); color: var(--white); }
  .photo-car {
    position: absolute; left: 0; right: 0; top: 130px; height: 340px;
    background: linear-gradient(170deg, #141416 0%, #2a2b30 30%, #0e0e10 55%, #3a3b40 75%, #111 100%);
  }
  .cover__title { position: absolute; top: 38px; left: 10px; right: 10px; text-align: center; font-size: 15px; font-weight: 600; line-height: 20px; }
  .cover__sub { position: absolute; top: 84px; left: 14px; right: 14px; text-align: center; font-size: 9px; line-height: 12px; color: var(--gold); }
  .panel--cover .brand { position: absolute; top: 435px; left: 0; right: 0; justify-content: center; }
  .panel--cover .brand__name { font-size: 15px; color: var(--white); }
  .panel--cover .brand__dot { background: var(--white); }

  /* Inside: tips */
  .panel--tips { width: 219px; background: var(--navy); color: var(--white); }
  .tips__title {
    position: absolute; top: 27px; left: 0; right: 0; height: 19px;
    background: var(--white); color: var(--navy); font-size: 11px; font-weight: 600;
    padding-left: 19px; line-height: 19px; text-transform: uppercase;
  }
  .tips__list { position: absolute; top: 56px; left: 12px; right: 14px; list-style: none; font-size: 8.6px; font-weight: 300; line-height: 10.9px; }
  .tips__list li { margin-bottom: 10.5px; }
  .tips__list b { color: var(--gold); font-weight: 600; }

  /* Inside: coverage */
  .panel--coverage { width: 219px; background: var(--white); }
  .illus-umbrella {
    position: absolute; top: 0; left: 0; right: 0; height: 208px;
    background: radial-gradient(ellipse at 50% 35%, #4d8fd6 0%, #9cc2ea 30%, #ffffff 62%);
  }
  .band {
    position: absolute; left: 0; right: 0; height: 20px; background: var(--navy);
    color: var(--gold); font-size: 11px; font-weight: 600; text-align: center; line-height: 20px; text-transform: uppercase;
  }
  .panel--coverage .band { top: 208px; }
  .coverage__body { position: absolute; top: 240px; left: 10px; right: 12px; font-size: 8.6px; font-weight: 300; line-height: 10.9px; }
  .coverage__body p { margin-bottom: 10px; }
  .coverage__body b { font-weight: 600; color: var(--navy-deep); }

  /* Inside: safety & contact */
  .panel--safety { width: 216px; background: var(--panel-grey); }
  .photo-driver {
    position: absolute; top: 0; left: 0; right: 0; height: 208px;
    background: linear-gradient(135deg, #8a7a66 0%, #c9b8a0 40%, #e8e2da 70%, #f6f4f0 100%);
  }
  .panel--safety .band--model { top: 208px; }
  .panel--safety .band--text { top: 278px; }
  .panel--safety .band--contact { top: 373px; }
  .safety__copy { position: absolute; left: 9px; right: 10px; font-size: 8.6px; font-weight: 300; line-height: 10.9px; }
  .safety__copy b { font-weight: 600; color: var(--navy-deep); }
  .safety__copy--buckle { top: 233px; }
  .safety__copy--text { top: 303px; }
  .safety__copy--text p { margin-bottom: 8px; }
  .contact {
    position: absolute; top: 410px; left: 0; right: 0; height: 76px; background: var(--navy);
    color: var(--white); text-align: center; font-size: 8.6px; line-height: 10.8px; padding-top: 6px;
  }
  .contact__name { font-weight: 600; }
</style>
</head>
<body>

<section class="sheet sheet--outside">
  <div class="panel panel--stats">
    <div class="photo-road" role="img" aria-label="Photo of a tree-lined country road at dusk"></div>
    <div class="stat stat--crashes">
      <div class="stat__over">OVER</div>
      <div class="stat__number">107,000</div>
      <div class="stat__caption">crashes will happen in the state of Arizona this year.</div>
    </div>
    <div class="stat stat--fatal">
      <div class="stat__over">OVER</div>
      <div class="stat__number">700</div>
      <div class="stat__caption">of them will result in fatalities.</div>
    </div>
    <div class="brand"><span class="brand__dot"></span><span class="brand__name">Marbren Legal</span></div>
    <p class="promise">If we don't win, you don't pay attorney fees. That seems fair to us. Know what's happening with your case, get the answers to your questions and work on getting better with the confidence that you've got an excellent group of <strong>people working for you.</strong></p>
  </div>

  <div class="panel panel--mailer">
    <div class="brand"><span class="brand__dot"></span><span class="brand__name">Marbren Legal</span></div>
    <p class="mailer__address">4870 N. Cedar Lane Suite B14<br>Phoenix AZ 85016</p>
  </div>

  <div class="panel panel--cover">
    <div class="photo-car" role="img" aria-label="Close-up photo of the front of a black car"></div>
    <h1 class="cover__title">Protect your family in case of a car accident</h1>
    <p class="cover__sub">A little knowledge and preparation go a long way</p>
    <div class="brand"><span class="brand__dot"></span><span class="brand__name">Marbren Legal</span></div>
  </div>
</section>

<section class="sheet sheet--inside">
  <div class="panel panel--tips">
    <h2 class="tips__title">Top 10 Tips to Avoid a Crash</h2>
    <ol class="tips__list">
      <li><b>1. Anyone making a left turn must wait for all oncoming traffic to clear before proceeding.</b> Yes, even if the light has turned yellow. Wait to be sure that all traffic has stopped.</li>
      <li><b>2. When your light turns green,</b> check to be sure that no vehicles are entering the intersection late.</li>
      <li><b>3. Allow plenty of room between you and the car in front of you.</b> Traffic can stop in an instant, even if you can't see anything ahead.</li>
      <li><b>4. Avoid being distracted.</b> Teenagers are especially susceptible to losing focus if there are too many friends in the car.</li>
      <li><b>5. Keep the volume of your radio down and never wear headphones.</b> Cars are very soundproof these days, but you need to be able to hear an ambulance or police siren.</li>
      <li><b>6. Be especially careful on the weekends and early morning hours.</b></li>
      <li><b>7. Don't speed.</b> Speed is a factor in most crashes. Street lights are timed and the freeway has traffic. It's likely you won't get there much faster even if you do speed.</li>
      <li><b>8. Don't drink and drive.</b> Many cab companies offer a free service to get you home safe.</li>
      <li><b>9. Use your turn signals.</b> This gives an early warning to vehicles you may not be able to see.</li>
    </ol>
  </div>

  <div class="panel panel--coverage">
    <div class="illus-umbrella" role="img" aria-label="Illustration of a blue umbrella sheltering a white car"></div>
    <h2 class="band">Have the Right Coverage</h2>
    <div class="coverage__body">
      <p>Many people don't know about the different kinds of insurance available. In addition to health insurance, we suggest:</p>
      <p><b>Auto Liability</b> (required by the state of Arizona in the amounts of $25,000 per person / $50,000 per accident, but a higher amount may be best ).</p>
      <p><b>Uninsured or Underinsured Motorist Coverage.</b> This protects YOU when the other driver doesn't have insurance or not enough.</p>
      <p><b>Medical Payments Coverage</b>. Up to $5,000 in coverage will be paid out to you no matter who is at fault in an accident and does not need to be reimbursed.</p>
      <p><b>Homeowners / Renters Insurance.</b> Protects you in case of injuries on your property as well as damage to your home from covered events.</p>
    </div>
  </div>

  <div class="panel panel--safety">
    <div class="photo-driver" role="img" aria-label="Photo of a smiling woman fastening her seat belt in a car"></div>
    <h2 class="band band--model">Model Safe Behavior</h2>
    <p class="safety__copy safety__copy--buckle"><b>Always buckle up.</b> Always put your children in car seats/boosters that are rated for their height and weight.</p>
    <h2 class="band band--text">Never Text While Driving</h2>
    <div class="safety__copy safety__copy--text">
      <p>Studies have shown that texting while driving is as dangerous as driving intoxicated.</p>
      <p><b>Show your children that no text is more important than your safety. It can wait.</b></p>
    </div>
    <h2 class="band band--contact">Contact Us</h2>
    <address class="contact" style="font-style:normal">
      <div class="contact__name">Marbren Legal Group</div>
      <div>4870 N. Cedar Lane Suite B14</div>
      <div>Phoenix AZ 85016</div>
      <div>602.555.0142</div>
      <div>info@marbrenlegal.com</div>
      <div>www.marbrenlegal.com</div>
    </address>
  </div>
</section>

</body>
</html>
```